Business Card Design Project

We are a innovative residential building company based in Sydney, Australia
our business name is MARLOWE HOMECRAFT SOLUTIONS PTY LTD.
Our company by line (please incorporate) "Our Business is Building!"
We specialise in creating high end innovative residential Alterations & Additions for our clients.
We would like to see original high end designs that are professional, striking, creative & have the WOW factor...
We like BLACK, BLUE, ORANGE, WHITE, SILVER... We would like to convey to our clients - professionalism/innovative approach/design/creativity/assurance/wow factor...

Target Market(s)

Clients who want/need residential alterations or additions to their homes.

Industry/Entity Type

Residential

Requirements
Must have
• LOGO
Bi Line (somewhere)
Name
Title
Phone number
Email address

Member of the RTA (Regional Trades Assn) Logo
Web Address - www.marlowehomecraft.com.au

Nice to have
• Fantail's are a small New Zealand bird and we would like to incorporate this as part of our new companies (double sided) business card. Whether it be the bird or just it's (fan) tail!
Should not have
• anything old-style.
we are looking for a contemporary, modern & striking Business Cards
clear strong colour accents
we had some stunning designs sent through, our favourites used the birds tail as an imprint on the card (not sure if that is clear of not)

```html
<!DOCTYPE html>
<html lang="en">
<head>
<meta charset="utf-8">
<title>Marlowe Homecraft Solutions – Business Card</title>
<link rel="stylesheet" href="https://fonts.googleapis.com/css2?family=Jost:wght@700&family=Arimo:wght@400;700&display=swap">
<style>
  :root {
    --brand-blue: #1a8fcf;
    --brand-orange: #f07a22;
    --silver: #a7a9ac;
    --paper: #ffffff;
    --stage: #d9d9d9;
    --ink-white: #ffffff;
  }
  * { box-sizing: border-box; margin: 0; padding: 0; }
  html, body {
    width: 1200px; height: 1096px; overflow: hidden;
    background: var(--stage);
  }
  .sheet {
    width: 1200px; height: 1096px;
    display: flex; flex-direction: column; align-items: center; justify-content: center;
    gap: 46px;
  }
  .card {
    position: relative;
    width: 840px; height: 480px;
    background: var(--paper);
    overflow: hidden;
    box-shadow: 0 6px 18px rgba(0,0,0,0.18);
  }
  .card-art { position: absolute; inset: 0; width: 100%; height: 100%; }

  .logo { display: flex; align-items: center; gap: 14px; }
  .logo-dot { border-radius: 50%; background: var(--silver); flex: none; }
  .logo-name {
    font-family: "Jost", "Futura", sans-serif; font-weight: 700;
    color: var(--brand-blue); line-height: 1.02; letter-spacing: 0.5px;
    white-space: nowrap;
  }
  .logo-name .line-sub { display: block; }

  .front .logo { position: absolute; left: 46px; top: 70px; }
  .front .logo-dot { width: 46px; height: 46px; }
  .front .logo-name { font-size: 31px; }
  .front .logo-name .line-sub { font-size: 21px; }

  .holder { position: absolute; left: 530px; top: 150px; font-family: "Arimo", Arial, sans-serif; }
  .holder-name { color: var(--brand-blue); font-weight: 700; font-size: 25px; }
  .holder-title { color: var(--brand-orange); font-size: 17px; margin-top: 2px; }

  .contacts {
    position: absolute; left: 44px; bottom: 30px; list-style: none;
    font-family: "Arimo", Arial, sans-serif; font-size: 18px; color: var(--ink-white);
  }
  .contacts li { display: flex; align-items: center; gap: 12px; height: 29px; }
  .contacts svg { width: 20px; height: 20px; flex: none; }

  .membership {
    position: absolute; right: 30px; bottom: 50px; display: flex; align-items: center; gap: 10px;
    font-family: "Arimo", Arial, sans-serif; font-size: 15px; color: var(--ink-white);
  }
  .membership-badge { width: 26px; height: 26px; background: var(--ink-white); }

  .back { background: radial-gradient(ellipse at 50% 48%, #ffffff 0%, #fafafa 35%, #dcdcdc 100%); }
  .back-lockup {
    position: absolute; inset: 0;
    display: flex; flex-direction: column; align-items: center; justify-content: center; gap: 26px;
  }
  .back .logo { gap: 22px; }
  .back .logo-dot { width: 78px; height: 78px; }
  .back .logo-name { font-size: 50px; }
  .back .logo-name .line-sub { font-size: 34px; }
  .byline {
    font-family: "Arimo", Arial, sans-serif; font-weight: 700; font-style: normal;
    font-size: 21px; color: var(--brand-orange); letter-spacing: 0.5px;
  }
</style>
</head>
<body>
<main class="sheet">

  <section class="card front" aria-label="Business card front">
    <svg class="card-art" viewBox="0 0 840 480" preserveAspectRatio="none" aria-hidden="true">
      <path d="M0,258 C150,214 270,226 430,306 C530,352 660,338 840,286 L840,480 L0,480Z" fill="var(--silver)"/>
      <path d="M0,272 C150,232 268,244 426,322 C526,368 656,352 840,300 L840,480 L0,480Z" fill="var(--brand-blue)"/>
      <path d="M420,316 C560,356 700,318 840,226 L840,258 C716,334 572,358 420,316Z" fill="var(--brand-orange)"/>
    </svg>

    <div class="logo">
      <span class="logo-dot"></span>
      <p class="logo-name">MARLOWE HOMECRAFT<span class="line-sub">SOLUTIONS PTY LTD.</span></p>
    </div>

    <div class="holder">
      <p class="holder-name">Your Name Here</p>
      <p class="holder-title">Position</p>
    </div>

    <ul class="contacts">
      <li>
        <svg viewBox="0 0 20 20" aria-hidden="true"><path d="M5 2 L8 2 L9 6 L7 8 C8 11 9 12 12 13 L14 11 L18 12 L18 15 C18 17 16 18 14 18 C8 17 3 12 2 6 C2 4 3 2 5 2Z" fill="none" stroke="#fff" stroke-width="1.6"/></svg>
        <span>02-5550-1842</span>
      </li>
      <li>
        <svg viewBox="0 0 20 20" aria-hidden="true"><rect x="5" y="2" width="10" height="6" fill="#fff"/><rect x="2" y="8" width="16" height="7" fill="#fff"/><rect x="5" y="13" width="10" height="5" fill="#fff" stroke="#1a8fcf"/></svg>
        <span>02-5550-1843</span>
      </li>
      <li>
        <svg viewBox="0 0 20 20" aria-hidden="true"><rect x="2" y="5" width="16" height="11" fill="#fff"/><path d="M2 5 L10 11 L18 5" fill="none" stroke="#1a8fcf" stroke-width="1.4"/></svg>
        <span>name@marlowehomecraft.com.au</span>
      </li>
      <li>
        <svg viewBox="0 0 20 20" aria-hidden="true"><circle cx="10" cy="10" r="7.5" fill="none" stroke="#fff" stroke-width="1.5"/><path d="M2.5 10 H17.5 M10 2.5 C6 6 6 14 10 17.5 M10 2.5 C14 6 14 14 10 17.5" fill="none" stroke="#fff" stroke-width="1.3"/></svg>
        <span>www.marlowehomecraft.com.au</span>
      </li>
    </ul>

    <div class="membership">
      <span>Member of the RTA</span>
      <span class="membership-badge"></span>
    </div>
  </section>

  <section class="card back" aria-label="Business card back">
    <div class="back-lockup">
      <div class="logo">
        <span class="logo-dot"></span>
        <p class="logo-name">MARLOWE HOMECRAFT<span class="line-sub">SOLUTIONS PTY LTD.</span></p>
      </div>
      <p class="byline">Our Business is Building!</p>
    </div>
  </section>

</main>
</body>
</html>
```